We need a business card design for a Dubai based company .

We need a business card for a Dubai based company called "Marwaneq Smoking Requisites Trading LLC". We mainly import Flavoured Tobacco products and Charcoal which is used for smoking in a Hookah/Shisha and distribute to the wholesalers and retailers. Logo file is attached herewith.

```html
<!DOCTYPE html>
<html lang="en">
<head>
<meta charset="utf-8">
<title>Marwaneq Business Card</title>
<link href="https://fonts.googleapis.com/css2?family=Roboto:wght@400;500&display=swap" rel="stylesheet">
<style>
  :root {
    --page-bg: #e9e5e1;
    --card-bg: #fbfbfb;
    --brand-red: #a8141c;
    --brand-red-dark: #8e0f16;
    --ink: #2a2a2a;
    --rule: #1f1f1f;
    --contact-ink: #f6dede;
  }
  * { margin: 0; padding: 0; box-sizing: border-box; }
  html, body {
    width: 1200px;
    height: 1054px;
    overflow: hidden;
    background: var(--page-bg);
    font-family: "Roboto", Arial, sans-serif;
  }
  .card {
    position: absolute;
    left: 100px;
    top: 226px;
    width: 1000px;
    height: 602px;
    border-radius: 26px;
    overflow: hidden;
    background: var(--card-bg);
    box-shadow: 0 10px 30px rgba(0,0,0,0.12);
  }
  .card-rule {
    position: absolute;
    left: 0; right: 0;
    top: 350px;
    height: 10px;
    background: var(--rule);
  }
  .card-band {
    position: absolute;
    left: 0; right: 0;
    top: 368px;
    bottom: 0;
    background: linear-gradient(180deg, var(--brand-red) 0%, var(--brand-red-dark) 100%);
  }
  .brand {
    position: absolute;
    left: 64px;
    top: 196px;
    color: var(--ink);
    font-weight: 400;
  }
  .brand-row { display: flex; align-items: center; gap: 16px; }
  .brand-mark {
    width: 22px; height: 22px;
    background: var(--brand-red);
  }
  .brand-name {
    font-size: 56px;
    letter-spacing: 6px;
    line-height: 1;
  }
  .brand-tagline {
    margin-top: 10px;
    font-size: 15px;
    letter-spacing: 3.4px;
    text-transform: uppercase;
    color: var(--brand-red);
  }
  .holder {
    position: absolute;
    right: 50px;
    top: 92px;
    text-align: right;
  }
  .holder-name {
    font-size: 33px;
    font-weight: 500;
    color: var(--brand-red);
    letter-spacing: 0.5px;
  }
  .holder-title {
    margin-top: 8px;
    font-size: 24px;
    color: var(--ink);
  }
  .contact {
    position: absolute;
    right: 50px;
    top: 406px;
    list-style: none;
    text-align: right;
    color: var(--contact-ink);
    font-size: 23px;
  }
  .contact li {
    display: flex;
    justify-content: flex-end;
    align-items: center;
    gap: 12px;
    height: 39px;
  }
  .contact svg { width: 22px; height: 22px; fill: var(--contact-ink); }
  .contact .no-icon { padding-right: 34px; }
</style>
</head>
<body>
  <div class="card">
    <div class="card-rule"></div>
    <div class="card-band" role="img" aria-label="Decorative red band with dark swoosh accent"></div>

    <div class="brand">
      <div class="brand-row">
        <span class="brand-mark"></span>
        <span class="brand-name">MARWANEQ</span>
      </div>
      <div class="brand-tagline">Smoking Requisites Trading LLC</div>
    </div>

    <div class="holder">
      <div class="holder-name">SAMIR HADDAD</div>
      <div class="holder-title">Managing Director</div>
    </div>

    <ul class="contact">
      <li>000-111-0000
        <svg viewBox="0 0 24 24"><path d="M4 9c0-3 3-5 8-5s8 2 8 5l-4 1-1-2H9L8 10 4 9zM6 12h12l2 7H4l2-7zm6 1.5a2.5 2.5 0 1 0 0 5 2.5 2.5 0 0 0 0-5z"/></svg>
      </li>
      <li>samir@marwaneq.com
        <svg viewBox="0 0 24 24"><path d="M2 5h20v14H2V5zm2 2v.5l8 5.5 8-5.5V7H4zm0 3v7h16v-7l-8 5.5L4 10z"/></svg>
      </li>
      <li>www.marwaneq.com
        <svg viewBox="0 0 24 24"><path d="M12 2a10 10 0 1 0 0 20 10 10 0 0 0 0-20zm0 2c1 1 2 3 2.3 5H9.7C10 7 11 5 12 4zM4.3 11h3.3c0 1 0 2 .1 2H4.3a8 8 0 0 1 0-2zm5.3 0h4.8v2H9.6v-2zm6.8 0h3.3a8 8 0 0 1 0 2h-3.4l.1-2zM9.7 15h4.6c-.3 2-1.3 4-2.3 5-1-1-2-3-2.3-5zM5 9a8 8 0 0 1 4-4c-.6 1-1 2.6-1.3 4H5zm10-4a8 8 0 0 1 4 4h-2.7c-.3-1.4-.7-3-1.3-4zM5 15h2.7c.3 1.4.7 3 1.3 4a8 8 0 0 1-4-4zm11.3 0H19a8 8 0 0 1-4 4c.6-1 1-2.6 1.3-4z"/></svg>
      </li>
      <li class="no-icon">P.O Box 00000, Dubai</li>
    </ul>
  </div>
</body>
</html>
```